Simple graphic needed from a brief word document about a business coaching training

I want the attached word doc information put into a visually appealing graphic that will look good in multiple size files for various marketing requirements

Orange and white are my main colours, but accents of purple, bright blue and bright green are good if you think it needs it

My business is in the social enterprise style so a professional but friendly look

Industry/Entity Type

Business

Logo Text

see word doc attached

```html
<!DOCTYPE html>
<html lang="en">
<head>
<meta charset="utf-8">
<title>The 5 C's for Successful Company Culture</title>
<link rel="stylesheet" href="https://fonts.googleapis.com/css2?family=Open+Sans:wght@400;600;700&display=swap">
<style>
  :root {
    --orange: #f15a2b;
    --purple: #5b2d8e;
    --white: #ffffff;
  }
  html, body {
    margin: 0;
    padding: 0;
    width: 763px;
    height: 1200px;
    overflow: hidden;
    background: var(--white);
  }
  .poster {
    display: block;
    width: 763px;
    height: 1200px;
  }
  .headline {
    font-family: "Open Sans", Arial, sans-serif;
    font-weight: 700;
    font-size: 106px;
    letter-spacing: -1.5px;
    fill: var(--orange);
  }
  .copyright-mark {
    font-family: "Open Sans", Arial, sans-serif;
    font-weight: 400;
    font-size: 42px;
    fill: var(--orange);
  }
  .subheadline {
    font-family: "Open Sans", Arial, sans-serif;
    font-weight: 400;
    font-size: 25px;
    letter-spacing: 8.2px;
    fill: var(--orange);
  }
  .stage-circle { fill: var(--orange); }
  .stage-label {
    font-family: "Open Sans", Arial, sans-serif;
    font-weight: 400;
    fill: var(--white);
    text-anchor: middle;
    dominant-baseline: central;
  }
  .stage-label--large { font-size: 31px; letter-spacing: 1px; }
  .stage-label--medium { font-size: 27px; letter-spacing: -0.3px; }
  .cycle-arrow {
    fill: none;
    stroke: var(--purple);
    stroke-width: 3.5;
  }
  .arrow-head { fill: var(--purple); }
  .brand-name {
    font-family: "Open Sans", Arial, sans-serif;
    font-weight: 600;
    font-size: 40px;
    fill: var(--orange);
  }
  .brand-tagline {
    font-family: "Open Sans", Arial, sans-serif;
    font-weight: 400;
    font-size: 14px;
    fill: var(--orange);
  }
  .brand-url {
    font-family: "Open Sans", Arial, sans-serif;
    font-weight: 400;
    font-size: 21px;
    fill: var(--orange);
  }
</style>
</head>
<body>
<svg class="poster" viewBox="0 0 763 1200" xmlns="http://www.w3.org/2000/svg" aria-labelledby="poster-title">
  <title id="poster-title">The 5 C's for successful company culture</title>
  <defs>
    <marker id="arrowhead" viewBox="0 0 10 10" refX="8" refY="5" markerWidth="5.5" markerHeight="5.5" orient="auto-start-reverse" markerUnits="strokeWidth">
      <path class="arrow-head" d="M0,0 L10,5 L0,10 z"/>
    </marker>
  </defs>

  <!-- Heading -->
  <text class="headline" x="36" y="107">the 5 C’s for</text>
  <text class="copyright-mark" x="443" y="36">©</text>
  <text class="subheadline" x="32" y="162">SUCCESFULL COMPANY CULTURE</text>

  <!-- Cycle arrows -->
  <g class="cycle">
    <path class="cycle-arrow" d="M445,400 Q478,418 505,443" marker-end="url(#arrowhead)"/>
    <path class="cycle-arrow" d="M562,635 Q558,672 545,706" marker-end="url(#arrowhead)"/>
    <path class="cycle-arrow" d="M374,806 Q336,811 294,804" marker-end="url(#arrowhead)"/>
    <path class="cycle-arrow" d="M132,706 Q120,672 116,627" marker-end="url(#arrowhead)"/>
    <path class="cycle-arrow" d="M171,435 Q202,408 238,390" marker-end="url(#arrowhead)"/>
  </g>

  <!-- Stages -->
  <g class="stage">
    <circle class="stage-circle" cx="340" cy="368" r="106"/>
    <text class="stage-label stage-label--large" x="340" y="366">Clarity</text>
  </g>
  <g class="stage">
    <circle class="stage-circle" cx="569" cy="527" r="106"/>
    <text class="stage-label stage-label--medium" x="572" y="527">Commitment</text>
  </g>
  <g class="stage">
    <circle class="stage-circle" cx="483" cy="792" r="106"/>
    <text class="stage-label stage-label--medium" x="485" y="792">Communication</text>
  </g>
  <g class="stage">
    <circle class="stage-circle" cx="191" cy="796" r="106"/>
    <text class="stage-label stage-label--medium" x="189" y="797">Collaboration</text>
  </g>
  <g class="stage">
    <circle class="stage-circle" cx="106" cy="521" r="106"/>
    <text class="stage-label stage-label--large" x="100" y="524">Creativity</text>
  </g>

  <!-- Brand block -->
  <g class="brand">
    <text class="brand-name" x="406" y="1097">Guiding Compass</text>
    <text class="brand-tagline" x="406" y="1121">Coaching Teams Toward Purposeful Workplaces</text>
    <text class="brand-url" x="406" y="1151">Guidingcompass.com.au</text>
  </g>
</svg>
</body>
</html>
```